Front page on www.brightvalemerch.com modern service ads - each ad for each featured service

We need to have initial 5 banners to be created for our soon to be launched new site,. These are 5 rotating banners that will showcase our companies key features. We are looking for a modern stylish yet simple look to highlight these features. Something thats very inviting and modern to fit the look of the new website.

5 banners need to be, information can be found on www.brightvalemerch.com about these. Please ask if any questions

Why us?
Art Services
Order Process
Current promotions
Clearance products

please also note. the design will be going onto this website. http://new.brightvalemerch.com/ Please base actual designs , color schemes etc.. for the new site.

Target Market(s)

Small businesses that purchase marketing promotional goods, to promote their business

Industry/Entity Type

Promotional Product

Font styles to use
Sans Serif

Requirements
Must have
• Size of the banner is 965 x 400 px
Nice to have
• Modern elements,, very clean and minimal look
Should not have
• no cheap generic clip art

```html
<!DOCTYPE html>
<html lang="en">
<head>
<meta charset="utf-8">
<title>Order Process – BrightvaleMerch</title>
<link href="https://fonts.googleapis.com/css2?family=Lato:wght@400;700&display=swap" rel="stylesheet">
<style>
  :root {
    --green: #6cb33f;
    --blue: #3b7dc0;
    --blue-button: #3d7ebf;
    --text: #2f2f2f;
    --bg: #ffffff;
    --bg-soft: #eceef0;
    --card: #b9855a;
    --steel: #c9ced3;
  }
  * { margin: 0; padding: 0; box-sizing: border-box; }
  html, body { width: 1200px; height: 497px; overflow: hidden; background: var(--bg); }
  body { font-family: "Lato", Arial, sans-serif; color: var(--text); }

  .banner { position: relative; width: 1200px; height: 497px; overflow: hidden; background: var(--bg); }

  .backdrop {
    position: absolute; left: 400px; top: 0; width: 520px; height: 497px;
    background: radial-gradient(ellipse at 50% 50%, var(--bg-soft) 0%, rgba(236,238,240,0.5) 45%, rgba(255,255,255,0) 75%);
  }

  .side-band {
    position: absolute; left: 0; top: 0; width: 83px; height: 497px; background: var(--green);
  }
  .side-title {
    position: absolute; left: 41px; top: 248px;
    transform: translate(-50%, -50%) rotate(-90deg);
    white-space: nowrap; color: #fff; font-size: 41px; font-weight: 400; letter-spacing: 0.5px;
  }

  .timeline { position: absolute; left: 0; top: 0; width: 1200px; height: 497px; }

  .icon { position: absolute; }
  .placeholder { position: absolute; border-radius: 12px; }
  .palette { left: 345px; top: 262px; width: 144px; height: 130px; border-radius: 50%;
    background: radial-gradient(circle at 45% 45%, #e0b47a, #c58e4e); }
  .clock { left: 742px; top: 268px; width: 134px; height: 134px; border-radius: 50%;
    background: radial-gradient(circle at 45% 40%, #ffffff 0%, #eef1f4 55%, var(--steel) 100%); }
  .parcel { left: 948px; top: 22px; width: 108px; height: 130px; border-radius: 6px;
    background: linear-gradient(160deg, #d9a874, var(--card)); }

  .step-label {
    position: absolute; transform: translateX(-50%); text-align: center;
    font-size: 17px; line-height: 24px; white-space: nowrap;
  }
  .step-label .accent { color: var(--blue); font-weight: 700; }

  .brand {
    position: absolute; left: 1013px; top: 318px; display: flex; align-items: center; gap: 6px;
    font-size: 18px; font-weight: 700; color: var(--text);
  }
  .brand-dot { width: 14px; height: 14px; border-radius: 50%; background: var(--green); }

  .cta {
    position: absolute; left: 1034px; top: 350px; width: 120px; height: 120px; border-radius: 50%;
    background: var(--blue-button); color: #fff; text-align: center;
    display: flex; flex-direction: column; justify-content: center; text-decoration: none;
  }
  .cta-main { font-size: 21px; font-weight: 700; line-height: 24px; }
  .cta-sub { font-size: 14px; line-height: 18px; }
</style>
</head>
<body>
<div class="banner">
  <div class="backdrop" role="img" aria-label="Faint photo of a hand holding a smartphone"></div>

  <div class="side-band"><div class="side-title">Order Process</div></div>

  <svg class="timeline" width="1200" height="497" viewBox="0 0 1200 497">
    <g stroke="var(--green)" stroke-width="2" fill="none">
      <line x1="221" y1="237" x2="1026" y2="237"/>
      <line x1="422" y1="237" x2="422" y2="262"/>
      <line x1="807" y1="237" x2="807" y2="262"/>
    </g>
    <g fill="var(--green)">
      <circle cx="221" cy="237" r="8"/>
      <circle cx="422" cy="237" r="8"/>
      <circle cx="613" cy="237" r="8"/>
      <circle cx="807" cy="237" r="8"/>
      <circle cx="1026" cy="237" r="8"/>
    </g>
  </svg>

  <!-- Step: call -->
  <svg class="icon phone-icon" style="left:165px;top:48px" width="112" height="104" viewBox="0 0 112 104">
    <rect x="22" y="28" width="82" height="70" rx="10" fill="#3a3a3a"/>
    <rect x="30" y="36" width="38" height="14" rx="2" fill="#8fa0a8"/>
    <g fill="#dcdcdc">
      <rect x="32" y="56" width="10" height="7" rx="1"/><rect x="46" y="56" width="10" height="7" rx="1"/><rect x="60" y="56" width="10" height="7" rx="1"/>
      <rect x="32" y="67" width="10" height="7" rx="1"/><rect x="46" y="67" width="10" height="7" rx="1"/><rect x="60" y="67" width="10" height="7" rx="1"/>
      <rect x="32" y="78" width="10" height="7" rx="1"/><rect x="46" y="78" width="10" height="7" rx="1"/><rect x="60" y="78" width="10" height="7" rx="1"/>
    </g>
    <rect x="4" y="6" width="20" height="92" rx="9" fill="#e6e6e6" stroke="#9a9a9a" stroke-width="2"/>
  </svg>
  <div class="step-label" style="left:221px;top:158px">Call us at<br><span class="accent">888-555-0142</span></div>

  <!-- Step: artwork -->
  <div class="placeholder palette" role="img" aria-label="Illustration of a painter's palette with a brush"></div>
  <div class="step-label" style="left:422px;top:408px">Email your artwork to<br><span class="accent">art@brightvalemerch.com</span></div>

  <!-- Step: approve -->
  <svg class="icon tick-icon" style="left:548px;top:10px" width="110" height="145" viewBox="0 0 110 145">
    <rect x="12" y="4" width="70" height="96" fill="#fafafa" stroke="#b8b8b8" stroke-width="2" transform="rotate(6 47 52)"/>
    <g stroke="#c0392b" stroke-width="3" fill="none">
      <rect x="20" y="16" width="12" height="12" stroke="#999" stroke-width="1.5"/>
      <polyline points="22,22 26,26 34,14"/>
      <rect x="20" y="40" width="12" height="12" stroke="#999" stroke-width="1.5"/>
      <polyline points="22,46 26,50 34,38"/>
    </g>
    <polyline points="40,108 62,130 104,76" fill="none" stroke="var(--green)" stroke-width="14" stroke-linecap="round" stroke-linejoin="round"/>
  </svg>
  <div class="step-label" style="left:613px;top:160px">Approve the design<br>for production</div>

  <!-- Step: processing -->
  <div class="placeholder clock" role="img" aria-label="Illustration of a silver wall clock"></div>
  <div class="step-label" style="left:807px;top:408px">We’ll process your order<br>within <span class="accent">24-48 hours</span></div>

  <!-- Step: delivery -->
  <div class="placeholder parcel" role="img" aria-label="Illustration of a cardboard shipping box"></div>
  <div class="step-label" style="left:1026px;top:160px">Track your order<br>untill it arrived at your door</div>

  <div class="brand"><span class="brand-dot"></span>BrightvaleMerch</div>

  <a class="cta" href="http://new.brightvalemerch.com/"><span class="cta-main">Click Here</span><span class="cta-sub">For More Info</span></a>
</div>
</body>
</html>
```